Business card design needed

the business is HR Consulting, but its for SME businesses who cant afford a permanent HR person. We sell an HR info system to help them meet minimum employment legislation but with this hope they then require us on a monthly subscription to phone or email us for HR advice. We are HR qualified mums working from home

So we will be partners to HR and Payroll systems known as unify HR and Tally

Target Market(s)

Small to medium businesses so not black and overly corporate, but having said that many are accounting businesses

Industry/Entity Type

Business

Contact Information for Business Card

Name of the company: Maple HR

Me:Marta Oldenbrook
Title:Managing Director

m: 0438 615 209
e: marta@maplehr.com.au
w: www.maplehr.com.au

What we do: HR Consulting, HR Systems and support, Payroll Advice

Requirements
Nice to have
• there is a company already out there known as Harbor professionals. I like the leaves at the end as I wanted something different like this to the usual business logos but still professional. I wanted a symbol to show calm, positive, ease flow going up ,etc. but realise they have the leaves and possibly cant copy, or can we?..( kite??, something calm and positive)dont know!!. Green and blue needed to be in it as nature and calm as well. I love the colours of www.staffingfundco.com ( attached the colours), as well as the calm wave line underneath. have a look as while they use green and blue I loved the purple colour thrown in there.Green and blue on their own are so overused. I want vibrant. I want double sided and when on a table I want it to stand out so maybe the purple colour (as per the colours on the fund website) solid on one side with just the 3 services we provide and personal and company name on front but need some creativity from you guys.

```html
<!DOCTYPE html>
<html lang="en">
<head>
<meta charset="utf-8">
<title>Maple HR – Business Card</title>
<link rel="stylesheet" href="https://fonts.googleapis.com/css2?family=Quicksand:wght@500;600&display=swap">
<style>
  :root {
    --paper: #ffffff;
    --wordmark: #2a8fa3;
    --contact: #1f8e9f;
    --band-green: #d6e8b4;
    --band-purple: #e2b8d8;
    --band-teal: #b3d6d2;
  }
  * { margin: 0; padding: 0; box-sizing: border-box; }
  html, body {
    width: 1200px;
    height: 1000px;
    overflow: hidden;
    background: var(--paper);
  }
  .card {
    position: relative;
    width: 1200px;
    height: 1000px;
    background: var(--paper);
    font-family: "Quicksand", "Helvetica Neue", Arial, sans-serif;
  }
  .decor-band {
    position: absolute;
    left: 0;
    top: 300px;
    width: 1200px;
    height: 255px;
    background: linear-gradient(90deg, var(--band-green) 0%, var(--band-purple) 50%, var(--band-teal) 100%);
  }
  .wordmark {
    position: absolute;
    left: 100px;
    top: 276px;
    font-size: 212px;
    font-weight: 600;
    line-height: 1;
    letter-spacing: 0;
    color: var(--wordmark);
    white-space: nowrap;
  }
  .contact {
    position: absolute;
    left: 107px;
    top: 574px;
    list-style: none;
    color: var(--contact);
    font-size: 37px;
    font-weight: 500;
    line-height: 51px;
    letter-spacing: 0.5px;
  }
  .contact .phone { font-size: 39px; }
</style>
</head>
<body>
  <div class="card">
    <div class="decor-band" role="img" aria-label="Flowing wave ribbons in green, purple and teal sweeping across the card"></div>

    <div class="wordmark">Maple HR</div>

    <ul class="contact">
      <li class="name">Marta Oldenbrook</li>
      <li class="title">Managing Director</li>
      <li class="phone">m: 0438.615.209</li>
      <li class="email">e: marta@maplehr.com.au</li>
      <li class="web">w: www.maplehr.com.au</li>
    </ul>
  </div>
</body>
</html>
```